Broschüre für innovatives Startup-Unternehmen in der Medizinbranche
Zielgruppe
RaV4 ist ein innovatives Startup-Unternehmen in der Medizinbranche. Sitz des Unternehmens ist Hof (in Bayern ganz oben :) )
RaV4 löst Probleme von heute und entwickelt zukunftsfähige Produkte, die dem Menschen das Leben erleichtern sollen.
RaV4 entwickelt und verwirklicht Ideen zu Produkten.
Aufgabenstellung
Weitere Bilder etc. werden nach Kontaktaufnahme übersendet.
Ich liebe Quitte Design!(Goldener Schnitt) ebenfalls schlichtes funktionelles Design, mit dem gewissen Etwas.
Ihr solltet euch mit Texten auskennen ich habe einen Anfang gemacht ihr sollt das ganze rundschleifen.
Sollten Fachliche Punkte eurer Meinung nach fehlen die dem Verständis des Lesers (Unternehmen) dienen bitte ich um Feedback dann liefern wir Entwürfe nach.
Unsere Zielgruppe sind aktuell überwiegend Frauen (in dem Fall Unternehmen), deshalb ist der Punkt Emotion auch nicht zu unterschätzen.
Diese sollten aber dennoch eine gewisse Sachlichkeit haben, da wir uns mit unseren Produkten in der Medizinbranche bewegen.
Die Broschüre soll zum ausprobieren unserer Produkte und Arbeitgeben und Unternehmer anregen über die Gesundheit ihrer Mitarbeiter un, sollte unserem Entwurf etwas an Logig fehlen , welche in eine Broschüre gehört die verkaufen soll ,bitte ich um Hinweis/Änderung.
Schriftarten die wir verwenden sind Georgia und Helvetica neue.
Unsere Produkte helfen Personen, die viel am Schreibtisch sitzen oder im Alltag/Arbeit oft einseitige Belastungen erfahren.
Hier findet ihr unsere Produkte: www.larvenquell.de
Eine Beispielbroschüre die uns gefällt und unser aktueller Flyer ist im Dateiupload hochgeladen.
Sie lösen Verspannungen auf höchst effektive und einfache Weise.
Ein Textentwurf wird hochgeladen,. Wir haben einen Anfang gewagt, sicher bringt ihr die Sache zur Perfektion!
Hier lasse ich mich auch gerne Überraschen.
Bildermaterial liefern wir so weit uns möglich. (Bilder sind noch nicht komplett und werden nach und nach hochgeladen.
Im Anschluß möchten wir alle Bearbeitungsdateien.
(indesign etc. alles was wir benötigen um im Nachgang noch etwas an der Broschüre zu verändern.)
Broschüregröße ist Din A5 Quer ?
Ich hoffe ich konnte mich einigermaßen ausd..

```html
<!DOCTYPE html>
<html lang="de">
<head>
<meta charset="utf-8">
<title>Broschüre – Welche Höhe ist für mich am besten geeignet?</title>
<link href="https://fonts.googleapis.com/css2?family=Roboto+Condensed:ital,wght@0,300;0,400;0,700;1,300;1,400;1,700&display=swap" rel="stylesheet">
<style>
  :root{
    --bg:#b3d4d4;
    --teal:#2fa5b6;
    --teal-dark:#2795a6;
    --teal-light:#4fc0d0;
    --white:#ffffff;
    --label:#2ba3b5;
    --muted:#8a8a8a;
  }
  *{margin:0;padding:0;box-sizing:border-box}
  html,body{width:1200px;height:700px;overflow:hidden;background:var(--bg)}
  body{font-family:"Roboto Condensed",Arial,sans-serif;position:relative}
  .spread{position:absolute;left:40px;top:152px;width:1120px;height:396px;display:flex;box-shadow:0 10px 30px rgba(0,0,0,.12)}
  .page{position:relative;width:560px;height:396px;overflow:hidden}
  .page--left{background:linear-gradient(90deg,var(--teal) 0%,var(--teal-dark) 60%,var(--teal-light) 96%,var(--teal) 100%);color:var(--white)}
  .page-title{position:absolute;left:62px;top:48px;font-size:25px;line-height:1.15;font-weight:700;font-style:italic}
  .page-title span{display:block;font-weight:300}
  .checklist{list-style:none;position:absolute;font-size:15px;font-weight:300;font-style:italic;line-height:1.3}
  .checklist li{position:relative;padding-left:34px;margin-bottom:20px}
  .checklist li svg{position:absolute;left:0;top:3px;width:22px;height:22px}
  .checklist--a{left:56px;top:128px;width:240px}
  .checklist--b{left:300px;top:128px;width:220px}
  .page--right{background:var(--teal)}
  .page--right svg{display:block}
  .spec-title{font-family:"Roboto Condensed",Arial,sans-serif;font-weight:700;font-size:10px;fill:var(--label)}
  .dim{font-family:"Roboto Condensed",Arial,sans-serif;font-size:6px;fill:var(--muted)}
</style>
</head>
<body>
<svg width="0" height="0" style="position:absolute">
  <defs>
    <symbol id="tick" viewBox="0 0 24 24">
      <circle cx="11" cy="13" r="9" fill="none" stroke="#fff" stroke-width="1.6" stroke-dasharray="46 12"/>
      <path d="M6 12.5l4 4L21 4" fill="none" stroke="#fff" stroke-width="2" stroke-linecap="round" stroke-linejoin="round"/>
    </symbol>
  </defs>
</svg>

<main class="spread">
  <section class="page page--left">
    <h1 class="page-title">Welche Höhe ist für mich am <span>besten geeignet?</span></h1>
    <ul class="checklist checklist--a">
      <li><svg><use href="#tick"/></svg>NEXIVA Groß ist vor allem für beleibtere Personen geeignet.</li>
      <li><svg><use href="#tick"/></svg>Um tiefer gelegene Rücken- und Gesäßmuskulatur zu erreichen, kann in diesem Bereich mit NEXIVA Groß gearbeitet werden.</li>
      <li><svg><use href="#tick"/></svg>NEXIVA Standard wird zur standardmäßgen Nutzung empfohlen.</li>
    </ul>
    <ul class="checklist checklist--b">
      <li><svg><use href="#tick"/></svg>NEXIVA Klein ist vor allem für Jugendliche und zierliche Personen geeignet.</li>
      <li><svg><use href="#tick"/></svg>Bei erheblichen Schmerzen im Brustwirbelsäulenbereich empfiehlt es sich, mit NEXIVA Klein zu beginnen.</li>
    </ul>
  </section>

  <section class="page page--right">
    <svg width="560" height="396" viewBox="0 0 560 396">
      <defs>
        <linearGradient id="panel" x1="0" y1="0" x2="1" y2="0">
          <stop offset="0" stop-color="#ffffff"/>
          <stop offset="1" stop-color="#e9eaea"/>
        </linearGradient>
        <linearGradient id="wood" x1="0" y1="0" x2="0" y2="1">
          <stop offset="0" stop-color="#ecd6bc"/>
          <stop offset="1" stop-color="#cfa981"/>
        </linearGradient>
      </defs>
      <path class="content-panel" d="M20 22 C70 100 80 270 52 368 L560 368 L560 22 Z" fill="url(#panel)"/>
      <line x1="18" y1="12" x2="560" y2="20" stroke="#fff" stroke-width="2"/>
      <line x1="52" y1="376" x2="560" y2="376" stroke="#fff" stroke-width="2"/>

      <text class="spec-title" x="540" y="48" text-anchor="end">ORBIS Tech Speech Comparison</text>
      <g class="dimension"><line x1="190" y1="62" x2="230" y2="62" stroke="#999" stroke-dasharray="1 1.5"/><text class="dim" x="210" y="58" text-anchor="middle">Cm 3,7</text></g>
      <g class="dimension"><line x1="400" y1="72" x2="432" y2="72" stroke="#999" stroke-dasharray="1 1.5"/><text class="dim" x="416" y="68" text-anchor="middle">Cm 2,7</text></g>
      <rect role="img" aria-label="Foto: ORBIS Holzblock mit Kerbe, 3,7 cm" x="122" y="68" width="190" height="122" rx="30" fill="url(#wood)"/>
      <rect role="img" aria-label="Foto: ORBIS Holzblock mit Kerbe, 2,7 cm" x="324" y="78" width="194" height="126" rx="30" fill="url(#wood)"/>

      <text class="spec-title" x="548" y="216" text-anchor="end">NEXIVA Tech Speech Comparison</text>
      <g class="dimension"><line x1="80" y1="258" x2="80" y2="322" stroke="#999" stroke-dasharray="1 1.5"/><text class="dim" transform="translate(78 312) rotate(-90)">Cm 5,0</text></g>
      <g class="dimension"><line x1="206" y1="240" x2="206" y2="318" stroke="#999" stroke-dasharray="1 1.5"/><text class="dim" transform="translate(204 300) rotate(-90)">Cm 6,0</text></g>
      <g class="dimension"><line x1="358" y1="236" x2="358" y2="322" stroke="#999" stroke-dasharray="1 1.5"/><text class="dim" transform="translate(356 300) rotate(-90)">Cm 8,0</text></g>
      <rect role="img" aria-label="Foto: NEXIVA Klein, Holzkeil mit Kerbe, 5 cm" x="88" y="266" width="108" height="50" rx="10" fill="url(#wood)"/>
      <rect role="img" aria-label="Foto: NEXIVA Standard, Holzkeil mit Kerbe, 6 cm" x="214" y="256" width="134" height="62" rx="10" fill="url(#wood)"/>
      <rect role="img" aria-label="Foto: NEXIVA Groß, Holzkeil mit Kerbe, 8 cm" x="368" y="248" width="152" height="76" rx="10" fill="url(#wood)"/>
    </svg>
  </section>
</main>
</body>
</html>
```